A5 Flyer for Christian Dating Agency for Church Notice Boards

Design brief
I write to tens of thousands of churches (of all denominations – ie Anglican, Methodist, Baptist, Evangelical, Catholic) every year and I send them an A5 flier to put up on their notice boards to ‘advertise’ or sign post the ‘single’ people (ie single never married, separated, divorced or widowed people) to my organisation ‘kindred7th’.
I’ve used a variety of designs in the past – and am now looking for a new design.
It’ll still be A5 and one sided.
It’ll be eye catching – it has to stand out on a notice board that probably has masses of other flyers/posters for all sorts of organisations/charities.
Vicars/church leaders will be happy to put it on their church notice board!
We have found in the past that using images of ‘happy couples’ is problematic – as people tend to identify with the pictures and then say “Well it’s obviously not for me as I’m not that colour, that age, etc” – or the images depict a certain type of person – that they aren’t – or they don’t fancy the person in the picture!
It needs to get across the very personal nature of our service – the fact that people aren’t a number or name on a database – but as members are known to us by name and we’ll get to know them through the course of their membership.
It needs to get across (probably by the professional great design) that we’re a professional organisation – not a cheap fly by night ‘just set up yesterday’ organisation. It needs to inspire confidence and trust because the people looking at it and thinking of contacting us will most likely never have done anything like this before (ie joined a dating agency) and in an ideal world would rather not have to!
So what I’m wanting is an A5 flyer that attracts and keeps peoples attention.
Within a very short space of time they will have realised we’re advertising a matchmaking/dating agency/organisation
They’ll get a sense of how we operate – and that we’re different to online sites
They feel comfortable and trusting of us
And most importantly they’ll be motivated to give us a call or look us up online.
Our telephone number is 0121 738 2961
Our web address is www.kindred7th.co.uk
*Background*
I run an OFF LINE Christian Dating and Introduction Agency. It’s off-line in that, although we have a website – which you’ll definitely want to have a look at to get a feel for our ‘brand’/ colour scheme etc as well as the flavour of who we are etc – we operate a totally off-line service. So we provide members details of other members by post and offer a very supportive service whereby my team and I are on the phone talking to, supporting, encouraging, listening, advising and helping members in any way we can to find their soul mate.
We’re a 100% stand alone Christian organisation. We only accept Christians onto our books – and Christians come to us because of that fact. They themselves are looking to meet other Christians who share their Christian faith.
We have members from late 20s right up to people in their 80s – and cater for all types of people – in terms of ethnicity, background, working life, location.
We are UK based and only cater for UK/Ireland members.
We charge a fee for our services – it’s an annual membership starting from £475 a year going up to £2127.
Everything we do is (we think!) different to online services and we like to set ourselves very apart from them. In our view (and this seems to be mirrored by the horror stories our members tell us of their experiences online) online sites are cheap to join, unreliable, full of non Christians (even if they say they are Christian sites), full of members that don’t really exist, full of people who aren’t really looking for a real friend or long term relationship (and this seems to be mirrored by the horror stories our members tell us of their experiences online).
We only want to attract Christians who are serious about finding new friends and companions and people who are looking to find a marriage partner long term.
We think we are the UK’s largest and most successful off line membership organisation (there’s no-one really doing what we’re doing – although we have lots of on-line competition).
We’ve been operating since 1999 and have had literally 100s of people get married through us – nearly 200 people in fact – and that’s only the ones we know about – we suspect there are many more.
We’re caring, professional, offer a raft of services like professional photo shoots, telephone coaching and materials to ensure that people don’t just get other members details but are successful in dating. (you can see our raft of services on our www.kindred7th.co.uk/join-now page)
You see the dating industry is littered with people NOT finding anyone – and it’s not because they aren’t eligible themselves but probably because they’re going about dating in the wrong way. It might seem the easiest thing in the world to do (because everyone’s doing it aren’t they?) whereas in fact it’s actually quite hard to do it right, to keep going after rejections and to find the right person for you. Everything we do is aimed to help people get it right and BE successful.
Reason: Would like to see amends to current designs as not yet fully decided which one to select and am awaiting changes
Target Market(s)
Single Christians - of all ages
Industry/Entity Type
Dating
Look and feel

```html
<!DOCTYPE html>
<html lang="en">
<head>
<meta charset="utf-8">
<title>kindred7th – A5 Church Notice Board Flyer</title>
<link rel="stylesheet" href="https://fonts.googleapis.com/css2?family=Montserrat:wght@300;400;600;700&family=Roboto:wght@300;400&display=swap">
<style>
  :root {
    --page-bg: #8ea6a6;
    --navy: #0f4a7c;
    --blue: #0b5a95;
    --blue-mid: #1a78c0;
    --blue-light: #3fa9e6;
    --sky-accent: #4fb0e6;
    --panel: #232325;
    --panel-text: #c4c4c4;
    --body-dark: #2f2f2f;
    --white: #ffffff;
    --head-font: "Montserrat", sans-serif;
    --body-font: "Roboto", sans-serif;
  }
  * { box-sizing: border-box; margin: 0; padding: 0; }
  html, body { width: 1200px; height: 960px; overflow: hidden; }
  body { background: var(--page-bg); position: relative; }

  .flyer {
    position: absolute; left: 280px; top: 27px;
    width: 694px; height: 982px;
    transform: scale(0.9216); transform-origin: 0 0;
    overflow: hidden; background: var(--white);
    box-shadow: 0 14px 30px rgba(0,0,0,.25);
  }
  .flyer-shapes { position: absolute; inset: 0; width: 694px; height: 982px; }
  .abs { position: absolute; }

  .headline { left: 31px; top: 366px; font-family: var(--head-font); color: var(--navy); }
  .headline-light { font-weight: 300; font-size: 31px; letter-spacing: 0.5px; line-height: 36px; color: #1f5f92; }
  .headline-bold { font-weight: 700; font-size: 29px; letter-spacing: 1px; line-height: 36px; }
  .tagline { left: 31px; top: 455px; font-family: var(--body-font); font-weight: 300; font-size: 16px; line-height: 19px; color: var(--body-dark); }

  .section-title { font-family: var(--head-font); font-weight: 700; color: var(--sky-accent); letter-spacing: 1px; }
  .why-title { left: 32px; top: 558px; font-size: 18.5px; }
  .what-title { left: 371px; top: 555px; font-size: 24px; }

  .feature { left: 32px; width: 300px; display: flex; gap: 14px; }
  .feature-icon { width: 50px; height: 46px; flex: none; }
  .feature-name { font-family: var(--head-font); font-weight: 700; font-size: 12.5px; letter-spacing: .6px; color: var(--sky-accent); margin-bottom: 5px; }
  .feature-text { font-family: var(--body-font); font-size: 7.6px; line-height: 9.8px; color: #e4e4e4; text-align: justify; width: 206px; }
  .f1 { top: 598px; } .f2 { top: 669px; } .f3 { top: 746px; } .f4 { top: 824px; }

  .what-copy { left: 373px; top: 596px; width: 290px; font-family: var(--body-font); font-size: 9.4px; line-height: 16.2px; color: var(--panel-text); text-align: justify; }
  .what-copy p + p { margin-top: 10.5px; }

  .price-pill { left: 377px; top: 753px; width: 284px; height: 60px; border-radius: 30px;
    background: linear-gradient(#d8d8d8, #9d9d9d); padding: 5px; }
  .price-inner { height: 50px; border-radius: 25px; display: flex; overflow: hidden;
    background: linear-gradient(#5cc0f2, #1d7fc4 55%, #176aa8); box-shadow: inset 0 1px 0 rgba(255,255,255,.5); }
  .price-label { flex: 1; padding: 8px 0 0 26px; }
  .price-caption { font-family: var(--head-font); font-weight: 600; font-size: 7px; color: #0c3558; letter-spacing: .3px; }
  .price-amount { font-family: var(--head-font); font-weight: 700; font-size: 23px; color: var(--white); letter-spacing: .8px; line-height: 26px; text-shadow: 0 1px 1px rgba(0,0,0,.35); }
  .price-toggle { width: 55px; border-left: 1px solid rgba(0,0,0,.25); display: flex; align-items: center; justify-content: center; }

  .phone { left: 388px; top: 828px; display: flex; align-items: center; gap: 9px;
    font-family: var(--head-font); font-weight: 600; font-size: 31px; color: var(--white); letter-spacing: .8px; }

  .website { left: 393px; top: 922px; font-family: var(--head-font); font-weight: 300; font-size: 17px; color: var(--white); letter-spacing: 4.3px; }
  .brand { left: 50px; top: 926px; display: flex; align-items: center; gap: 8px;
    font-family: var(--head-font); font-weight: 600; font-size: 32px; color: var(--white); letter-spacing: -0.5px; }
  .brand-dot { width: 18px; height: 18px; border-radius: 50%; background: var(--white); }
</style>
</head>
<body>
<main class="flyer">
  <svg class="flyer-shapes" viewBox="0 0 694 982" xmlns="http://www.w3.org/2000/svg">
    <defs>
      <linearGradient id="sunset" x1="0" y1="0" x2="0" y2="1">
        <stop offset="0" stop-color="#e58a4a"/>
        <stop offset=".42" stop-color="#e2674a"/>
        <stop offset=".55" stop-color="#8a8a96"/>
        <stop offset=".72" stop-color="#c9cbd1"/>
        <stop offset=".9" stop-color="#f2f2f2"/>
        <stop offset="1" stop-color="#f7f7f7"/>
      </linearGradient>
      <linearGradient id="evening" x1="0" y1="0" x2="0" y2="1">
        <stop offset="0" stop-color="#b37d80"/>
        <stop offset=".3" stop-color="#c4978f"/>
        <stop offset=".55" stop-color="#5e4448"/>
        <stop offset="1" stop-color="#2a2224"/>
      </linearGradient>
    </defs>

    <rect class="photo-sunset" x="0" y="0" width="694" height="530" fill="url(#sunset)" role="img" aria-label="Photo: people paddleboarding on the sea at sunset"/>
    <g class="light-streaks" stroke="#fff" stroke-opacity=".75">
      <line x1="340" y1="0" x2="268" y2="110" stroke-width="2"/>
      <line x1="330" y1="0" x2="262" y2="104" stroke-width="1.4"/>
      <line x1="320" y1="0" x2="255" y2="100" stroke-width="1"/>
    </g>

    <rect class="panel-dark" x="0" y="530" width="694" height="452" fill="var(--panel)"/>
    <polygon class="facet-light" points="382,352 287,530 694,530 694,600" fill="var(--blue-mid)"/>
    <polygon class="facet-deep" points="470,440 420,530 560,530" fill="#0d5f9c"/>
    <polygon class="chevron-band" points="354,0 432,0 317,182 694,562 694,662 232,182" fill="var(--blue)"/>
    <polygon class="photo-couple" points="432,0 694,0 694,562 317,182" fill="url(#evening)" role="img" aria-label="Photo: a couple sitting together by a lake at dusk, seen from behind"/>

    <line class="divider" x1="338" y1="547" x2="338" y2="842" stroke="#3d3d40" stroke-width="1"/>

    <polygon class="footer-right" points="370,882 694,882 694,982 312,982" fill="var(--blue-mid)"/>
    <polygon class="footer-edge" points="362,882 376,882 318,982 304,982" fill="var(--blue-light)"/>
    <polygon class="footer-left" points="0,907 348,907 305,982 0,982" fill="var(--navy)"/>
    <rect class="footer-strip" x="0" y="972" width="694" height="10" fill="var(--blue-light)"/>
  </svg>

  <h1 class="abs headline">
    <span class="headline-light" style="display:block">Fed up of being</span>
    <span class="headline-bold" style="display:block">ON YOUR OWN?</span>
  </h1>
  <p class="abs tagline">A 100% ‘stand alone’ organisation<br>bringing Christians together off-line</p>

  <h2 class="abs section-title why-title">WHY WE ARE DIFFERENT</h2>

  <div class="abs feature f1">
    <svg class="feature-icon" viewBox="0 0 50 46" fill="var(--blue-light)">
      <ellipse cx="25" cy="38" rx="23" ry="6" fill="none" stroke="var(--blue-light)" stroke-width="2.5"/>
      <circle cx="13" cy="14" r="5"/><circle cx="37" cy="14" r="5"/>
      <path d="M4 32c0-8 4-12 9-12s9 4 9 12z"/><path d="M28 32c0-8 4-12 9-12s9 4 9 12z"/>
      <circle cx="25" cy="12" r="7" stroke="var(--panel)" stroke-width="1.5"/>
      <path d="M13 36c0-11 5-16 12-16s12 5 12 16z" stroke="var(--panel)" stroke-width="1.5"/>
    </svg>
    <div>
      <h3 class="feature-name">GENUINE MEMBERS</h3>
      <p class="feature-text">We only accept genuine Christians as members so if that’s what you’re looking for you’ll be in the right company with us.</p>
    </div>
  </div>

  <div class="abs feature f2">
    <svg class="feature-icon" viewBox="0 0 50 46" fill="none" stroke="var(--blue-light)" stroke-width="2.5">
      <rect x="2" y="7" width="46" height="32"/>
      <path d="M2 7l23 19 23-19M2 39l17-17M48 39L31 22"/>
    </svg>
    <div>
      <h3 class="feature-name">OFF LINE</h3>
      <p class="feature-text">Our membership and introduction service is provided entirely off line. You can call it old fashioned or you can sigh with relief that you’ve found a truly personal, interactive and effective way of meeting other single Christians.</p>
    </div>
  </div>

  <div class="abs feature f3">
    <svg class="feature-icon" viewBox="0 0 50 46" fill="none" stroke="var(--blue-light)" stroke-width="3">
      <path d="M12 13A18 18 0 1 1 8 31"/>
      <path d="M4 18l8-6 3 9" stroke-width="2.5"/>
      <path d="M26 12v12l7 5"/>
    </svg>
    <div>
      <h3 class="feature-name">COMMITMENT</h3>
      <p class="feature-text">Both yours, other members and ours. You won’t find ‘here today, gone tomorrow’ members on our books. Just real genuine Christians who are truly committed to finding new friends and the right partner</p>
    </div>
  </div>

  <div class="abs feature f4">
    <svg class="feature-icon" viewBox="0 0 50 46" fill="none" stroke="var(--blue-light)" stroke-width="2.5">
      <circle cx="25" cy="14" r="8"/>
      <circle cx="25" cy="14" r="12" stroke-dasharray="4 3"/>
      <path d="M5 45c0-11 9-17 20-17s20 6 20 17z"/>
      <path d="M25 29v12"/>
    </svg>
    <div>
      <h3 class="feature-name">EXPERT SUPPORT</h3>
      <p class="feature-text">“It ain’t what you do, it’s the way that you do it, and that’s what gets results.” We don’t soley introduce Christians to each other – we provide tools, education, coaching and support to make sure you’re doing the right things in the right way. That’s what gets results!</p>
    </div>
  </div>

  <h2 class="abs section-title what-title">WHAT WE DO</h2>
  <div class="abs what-copy">
    <p>We simply and effectively connect you with other single Christians across the UK and Ireland in a personal way that encourages and helps you to make new friends.</p>
    <p>We operate entirely OFF LINE with real staff dedicated to each members individual circumstances and success. As a member you will benefit from our caring, hands-on approach and enjoy our whole-hearted commitment to helping you find your soul mate. Click the play button to the left to watch the story.</p>
  </div>

  <div class="abs price-pill">
    <div class="price-inner">
      <div class="price-label">
        <p class="price-caption">ANNUAL MEMBERSHIP STARTING FROM</p>
        <p class="price-amount">£475 A YEAR</p>
      </div>
      <div class="price-toggle">
        <svg width="16" height="9" viewBox="0 0 16 9"><path d="M0 0h16L8 9z" fill="#0c3558"/></svg>
      </div>
    </div>
  </div>

  <p class="abs phone">
    <svg width="26" height="26" viewBox="0 0 24 24" fill="var(--sky-accent)"><path d="M6.6 10.8a15 15 0 0 0 6.6 6.6l2.2-2.2c.3-.3.7-.4 1-.2 1.1.4 2.3.6 3.6.6.6 0 1 .4 1 1V20c0 .6-.4 1-1 1A17 17 0 0 1 3 4c0-.6.4-1 1-1h3.5c.6 0 1 .4 1 1 0 1.3.2 2.5.6 3.6.1.3 0 .7-.2 1z"/></svg>
    0121 738 2961
  </p>

  <p class="abs brand"><span class="brand-dot"></span>kindred7th</p>
  <p class="abs website">www.kindred7th.co.uk</p>
</main>
</body>
</html>
```